brochure for payroll services

we need a brochure design for our new payroll services- either to be send to prospect as an email attachment or print. see attached on content required.
our corporate colour is orange . the design should communicate trust ,and reliability with a breadth of fresh air.

```html
<!DOCTYPE html>
<html lang="en">
<head>
<meta charset="utf-8">
<title>Payroll Services Brochure</title>
<link href="https://fonts.googleapis.com/css2?family=Lato:wght@300;400;700&display=swap" rel="stylesheet">
<style>
  :root{
    --orange:#f58a35;
    --orange-deep:#ef7d22;
    --ink:#3a3a3a;
    --ink-soft:#4a4a4a;
    --rule:#555;
    --paper:#ffffff;
    --band-text:#fde3cc;
  }
  *{margin:0;padding:0;box-sizing:border-box}
  html,body{width:1200px;height:875px;overflow:hidden;background:var(--paper)}
  body{font-family:"Lato",sans-serif;color:var(--ink);position:relative}
  .brochure{position:relative;width:1200px;height:875px;border:1px solid var(--rule)}
  .panel{position:absolute;top:0;height:100%}
  .panel--intro{left:0;width:400px;border-right:1px solid var(--rule)}
  .panel--scope{left:400px;width:400px;border-right:1px solid var(--rule)}
  .panel--related{left:800px;width:400px}

  .accent-bar{position:absolute;left:0;top:79px;width:39px;height:101px;background:var(--orange)}
  .intro-title{position:absolute;left:52px;top:70px;width:320px;font-size:28px;line-height:37px;font-weight:400;color:var(--orange)}
  .intro-text{position:absolute;left:52px;top:223px;width:296px;font-size:15px;line-height:28.5px;text-align:justify;color:var(--ink-soft)}

  .section-head{position:absolute;display:flex;align-items:center;gap:9px;color:var(--orange);font-size:28px;font-weight:400}
  .section-head svg{width:36px;height:36px;flex:none}
  .advantages-head{left:48px;top:462px}
  .scope-head{left:452px;top:77px;position:absolute}

  .advantages{position:absolute;left:52px;top:527px;width:296px;list-style:none}
  .advantages li{font-size:15px;line-height:21.5px;text-align:justify;color:var(--ink-soft);margin-bottom:21px}
  .advantages li::before{content:"• "}

  .scope-intro{position:absolute;left:54px;top:137px;font-size:16px;line-height:22px;color:var(--ink-soft)}
  .scope-list{position:absolute;left:45px;top:222px;width:340px;list-style:none;display:flex;flex-direction:column;gap:19px}
  .scope-list li{font-size:15.5px;line-height:21px;color:var(--ink-soft);display:flex}
  .scope-list b{font-weight:700;width:14px;flex:none}

  .art-dollar{position:absolute;left:113px;top:705px;width:142px;height:121px;border-radius:10px;background:radial-gradient(circle at 55% 40%,#f3d43a,#d6b52a 55%,#cfd9d3 80%,#fff 100%)}

  .related-band{position:absolute;left:0;top:0;width:400px;height:481px;background:var(--orange)}
  .related-title{position:absolute;left:63px;top:82px;font-size:28px;font-weight:400;color:#fff}
  .related-list{position:absolute;left:63px;top:160px;width:320px;list-style:none;font-size:15.5px;line-height:40px;color:var(--band-text)}
  .related-list li{text-indent:-0px}
  .related-list .wrap{padding-left:12px;display:block}
  .photo{position:absolute}
  .photo--calculator{left:0;top:327px;width:198px;height:128px;background:linear-gradient(135deg,#e9eef3,#b9c4cf 60%,#59606a)}
  .photo--savings{left:205px;top:327px;width:195px;height:128px;background:linear-gradient(135deg,#f4f4f4,#dcdcdc 55%,#e9a4b4)}
  .photo--accounting{left:0;top:481px;width:400px;height:394px;background:radial-gradient(circle at 40% 35%,#6c7b8a,#3c4753 60%,#252c33)}
</style>
</head>
<body>
<main class="brochure">

  <section class="panel panel--intro">
    <div class="accent-bar"></div>
    <h1 class="intro-title">Peace of mind for you to allow you to focus on your core activities.</h1>
    <p class="intro-text">So that you will not be distracted by technology selection, implementation and maintenance, attracting and retaining expertise and dedicated resources, keeping track of changes in regulations and potential conflict of interests within (knowing the salary and benefits for all).</p>

    <h2 class="section-head advantages-head">
      <svg viewBox="0 0 36 36" aria-hidden="true"><circle cx="18" cy="18" r="17" fill="var(--orange)"/><path d="M11 25 L24 12 M14 12 H24 V22" stroke="#fff" stroke-width="3.4" fill="none" stroke-linecap="square"/></svg>
      Our advantages
    </h2>
    <ul class="advantages">
      <li>Project management and methodology to ensure seamless transition and sustainable delivery</li>
      <li>Domain knowledge in payroll, accounting &amp; finance and tax</li>
      <li>Robust technology platform for automation, control and visibility</li>
      <li>Proven delivery expertise and experience to provide reliable and trusted services</li>
    </ul>
  </section>

  <section class="panel panel--scope">
    <h2 class="section-head scope-head">
      <svg viewBox="0 0 36 36" aria-hidden="true"><circle cx="18" cy="18" r="17" fill="var(--orange)"/><path d="M11 25 L24 12 M14 12 H24 V22" stroke="#fff" stroke-width="3.4" fill="none" stroke-linecap="square"/></svg>
      Scope of services
    </h2>
    <p class="scope-intro">The scope of services include<br>the following :</p>
    <ol class="scope-list">
      <li><b>1.</b><span>Process payroll (salary calculation) on monthly to bi-monthly (ie. twice a month) basis</span></li>
      <li><b>2.</b><span>Process gross to net salary and applicable CPF, CDAC, MBMF, SINDA or ECF contribution</span></li>
      <li><b>3.</b><span>Process bonuses, and any adhoc payments</span></li>
      <li><b>4.</b><span>Process no pay leave</span></li>
      <li><b>5.</b><span>Salary disbursement to employees via Bank GIRO transfer</span></li>
      <li><b>6.</b><span>Provide payroll report for management's review</span></li>
      <li><b>7.</b><span>Prepare and submit CPF e-submission</span></li>
      <li><b>8.</b><span>Prepare and submit year-end tax forms (Form IR8A)</span></li>
    </ol>
    <div class="art-dollar" role="img" aria-label="Illustration of a gold dollar sign resting on cheques"></div>
  </section>

  <section class="panel panel--related">
    <div class="related-band"></div>
    <h2 class="related-title">Other related services</h2>
    <ul class="related-list">
      <li>•Employee’s leave administration and<span class="wrap">management</span></li>
      <li>•Timesheet management</li>
      <li>•Claim management</li>
    </ul>
    <div class="photo photo--calculator" role="img" aria-label="Photo of hands using a calculator beside coins"></div>
    <div class="photo photo--savings" role="img" aria-label="Photo of a businesswoman at a desk with a piggy bank"></div>
    <div class="photo photo--accounting" role="img" aria-label="Photo of a businessman writing accounting terms on a glass board"></div>
  </section>

</main>
</body>
</html>
```